"Bright Hollow Craft Dwellings" need a busines Card Design got Builder

We need a business card design for a company based in Milford, Michigancalled Bright Hollow Craft Dwellings - has been recognized as a premier custom home builder. Distinguished by outstanding craftmanship and timeless beauty. Our custom home can be found in the most prestigious communities in Michigan. The homes are built with ICF (insulated concrete homes) which is green, allergy free, fire free, mold free and quitter. Our slogan "Shaping every home with care" and also we are ICF distributor for the state of Michigan

Target Market(s)

Anyone who is making over $100,000 a year and who wants to have totally custom built home. Ages from 29 up to 60 years old

Industry/Entity Type

Concrete

Contact Information for Business Card

we want to use - green, black, gray or blue colors - we want to look different with our business cards, because we built homes only with ICF, green, healthier and highly energy efficient homes.

Requirements
Must have
• I have logo that I attached and we have been using the logo (the only green home)
Nice to have
• should look quality business card,

```html
<!DOCTYPE html>
<html lang="en">
<head>
<meta charset="utf-8">
<title>Bright Hollow Craft Dwellings – Business Card</title>
<link href="https://fonts.googleapis.com/css2?family=Lato:wght@300;400;700;900&display=swap" rel="stylesheet">
<style>
  :root {
    --backdrop: #2a2a2c;
    --card: #ffffff;
    --card-shade: #eceef1;
    --navy: #2b2170;
    --blue: #2a8ee6;
    --ink: #5b5b63;
    --mark-grey: #6d6d74;
  }
  * { box-sizing: border-box; margin: 0; padding: 0; }
  html, body { width: 1200px; height: 873px; overflow: hidden; }
  body {
    background: var(--backdrop);
    font-family: "Lato", sans-serif;
    position: relative;
  }
  .card {
    position: absolute;
    width: 520px;
    height: 297px;
    background: linear-gradient(160deg, var(--card) 40%, var(--card-shade));
    overflow: hidden;
    box-shadow: 0 14px 30px rgba(0,0,0,.45);
  }
  .card--back { left: 70px; top: 120px; }
  .card--front { left: 610px; top: 440px; }

  .card__band { position: absolute; left: 0; bottom: 0; width: 100%; height: 40px; }

  .wordmark {
    position: absolute;
    display: flex;
    align-items: center;
    gap: 14px;
  }
  .wordmark__dot {
    width: 44px; height: 44px;
    border-radius: 50%;
    background: var(--navy);
    flex: none;
  }
  .wordmark__name {
    font-weight: 400;
    color: var(--mark-grey);
    text-transform: uppercase;
    letter-spacing: 2px;
    line-height: 1.05;
    font-size: 19px;
    white-space: nowrap;
  }
  .card--back .wordmark { left: 74px; top: 104px; }
  .card--front .wordmark { left: 250px; top: 40px; }
  .card--front .wordmark__dot { width: 38px; height: 38px; }
  .card--front .wordmark__name { font-size: 16px; }

  .slogan {
    position: absolute;
    left: 232px; top: 192px;
    color: var(--blue);
    font-weight: 700;
    font-size: 13px;
    letter-spacing: 1px;
    text-transform: uppercase;
    white-space: nowrap;
  }

  .person { position: absolute; left: 330px; top: 128px; }
  .person__name { color: var(--navy); font-weight: 900; font-size: 19px; white-space: nowrap; }
  .person__role { color: #333; font-size: 14px; margin-top: 2px; }

  .icon-rail {
    position: absolute;
    left: 0; top: 120px;
    width: 40px; height: 150px;
    background: var(--navy);
    border-radius: 0 10px 10px 0;
    display: flex; flex-direction: column;
    justify-content: space-around; align-items: center;
    padding: 8px 0;
  }
  .icon-rail svg { width: 18px; height: 18px; }

  .contact-list {
    position: absolute;
    left: 56px; top: 124px;
    list-style: none;
    color: var(--ink);
    font-weight: 700;
    font-size: 13px;
  }
  .contact-list li { height: 28px; line-height: 28px; white-space: nowrap; }
</style>
</head>
<body>

<section class="card card--back">
  <div class="wordmark">
    <span class="wordmark__dot"></span>
    <span class="wordmark__name">Bright Hollow<br>Craft Dwellings</span>
  </div>
  <p class="slogan">Shaping every home with care</p>
  <svg class="card__band" viewBox="0 0 520 40" preserveAspectRatio="none">
    <path d="M350 12 Q352 4 370 4 L520 4 L520 40 L350 40 Z" fill="var(--navy)"/>
    <rect x="0" y="28" width="520" height="12" fill="var(--blue)"/>
  </svg>
</section>

<section class="card card--front">
  <div class="wordmark">
    <span class="wordmark__dot"></span>
    <span class="wordmark__name">Bright Hollow<br>Craft Dwellings</span>
  </div>

  <div class="person">
    <p class="person__name">Daniel Vorhees</p>
    <p class="person__role">Owner / Founder</p>
  </div>

  <div class="icon-rail" aria-hidden="true">
    <svg viewBox="0 0 18 18"><rect x="5" y="1.5" width="8" height="15" rx="1.5" fill="none" stroke="#fff" stroke-width="1.6"/></svg>
    <svg viewBox="0 0 18 18"><rect x="5" y="2" width="8" height="4" fill="#fff"/><rect x="2" y="6" width="14" height="7" rx="1" fill="#fff"/><rect x="5" y="11" width="8" height="5" fill="#fff" stroke="var(--navy)" stroke-width="1"/></svg>
    <svg viewBox="0 0 18 18"><rect x="2" y="7" width="9" height="5" rx="2.5" transform="rotate(-45 6.5 9.5)" fill="none" stroke="#fff" stroke-width="1.6"/><rect x="7" y="6" width="9" height="5" rx="2.5" transform="rotate(-45 11.5 8.5)" fill="none" stroke="#fff" stroke-width="1.6"/></svg>
    <svg viewBox="0 0 18 18"><rect x="1.5" y="4" width="15" height="10" fill="#fff"/><path d="M1.5 4 L9 10 L16.5 4" fill="none" stroke="var(--navy)" stroke-width="1.3"/></svg>
    <svg viewBox="0 0 18 18"><path d="M9 17 C4 11 3.5 9 3.5 7 A5.5 5.5 0 0 1 14.5 7 C14.5 9 14 11 9 17 Z" fill="#fff"/><circle cx="9" cy="7" r="2" fill="var(--navy)"/></svg>
  </div>

  <ul class="contact-list">
    <li>555.214.0187</li>
    <li>555.386.4410</li>
    <li>hello@brighthollowcraft</li>
    <li>www.brighthollowcraft.com</li>
    <li>4120 Linden Ridge Rd, Suite 12, Milford MI</li>
  </ul>

  <svg class="card__band" viewBox="0 0 520 40" preserveAspectRatio="none">
    <path d="M350 12 Q352 4 370 4 L520 4 L520 40 L350 40 Z" fill="var(--navy)"/>
    <rect x="0" y="28" width="520" height="12" fill="var(--blue)"/>
  </svg>
</section>

</body>
</html>
```